Website for a printing company - Wordpress

We are a printing company and would like to have a new website.

Here you will find our current.
www.grijsdrukhuis.be
not professional, and does not stand out.

We are looking for something, sleek, modern, but also enthusiastic, young & dynamic!

We do not want to offer our complete catalog on our website, but we do want customers to know clearly that we can print anything.

It's all in the details.

Requirements
Must have
• counters with example
already served 500 customers
already printed 300 paper sheets
etc.

```html
<!DOCTYPE html>
<html lang="en">
<head>
<meta charset="utf-8">
<title>Grey Print House – Printing &amp; graphic agency</title>
<link rel="stylesheet" href="https://fonts.googleapis.com/css2?family=Rajdhani:wght@600;700&family=Rubik:ital,wght@0,300;0,400;0,500;1,300&display=swap">
<style>
:root{
  --black:#131313;
  --ink:#1c1c1c;
  --white:#ffffff;
  --orange:#ec6a0e;
  --grey:#7a7a7a;
  --light:#f4f4f4;
  --head:"Rajdhani",sans-serif;
  --body:"Rubik",sans-serif;
}
*{box-sizing:border-box;margin:0;padding:0}
html,body{width:1200px;height:3309px;overflow:hidden}
body{position:relative;background:var(--white);font-family:var(--body);color:var(--ink)}
.abs{position:absolute}

/* header */
.site-header{position:absolute;left:0;top:0;width:1200px;height:70px;background:var(--white)}
.brand{position:absolute;left:144px;top:14px;font-family:var(--head);font-weight:700;font-size:38px;letter-spacing:-.5px;color:var(--black);line-height:42px}
.main-nav{position:absolute;top:28px;left:0;font-family:var(--head);font-weight:700;font-size:14px;color:var(--black)}
.main-nav a{position:absolute;white-space:nowrap;color:inherit;text-decoration:none}
.main-nav a.active::after{content:"";position:absolute;left:0;right:0;top:20px;height:2px;background:var(--orange)}
.header-phone{position:absolute;left:0;top:0}
.header-phone-text{position:absolute;left:966px;top:22px;font-family:var(--head);font-weight:700;font-size:19px;color:var(--white)}

/* hero */
.hero{position:absolute;left:0;top:70px;width:1200px;height:564px;background:radial-gradient(ellipse at 40% 40%,#8a8a8a 0%,#4a4a4a 55%,#2a2a2a 100%)}
.hero-title{position:absolute;left:0;width:1200px;top:155px;text-align:center;font-family:var(--head);font-weight:700;font-size:84px;color:var(--white);letter-spacing:1px;line-height:90px}
.hero-sub{position:absolute;left:0;width:1200px;top:262px;text-align:center;font-family:var(--head);font-weight:700;font-size:26px;color:var(--white)}
.btn{position:absolute;height:55px;border-radius:28px;font-family:var(--head);font-weight:700;font-size:17px;color:var(--white);display:flex;align-items:center;justify-content:center;gap:10px}
.btn-quote{left:392px;top:335px;width:201px;background:var(--orange)}
.btn-more{left:607px;top:335px;width:201px;background:var(--black)}
.slide-arrow{position:absolute;top:256px;width:52px;height:52px;border-radius:50%;background:rgba(20,20,20,.85)}

/* welcome */
.section-title{position:absolute;left:0;width:1200px;text-align:center;font-family:var(--head);font-weight:700;font-size:39px;color:var(--black)}
.welcome-text{position:absolute;left:225px;width:750px;top:800px;text-align:center;font-size:12.5px;line-height:27px;color:var(--grey);font-weight:300}

/* dark bands */
.dark-band{position:absolute;left:0;width:1200px;background:linear-gradient(135deg,#2c2c2c 0%,#141414 40%,#111 70%,#2a2a2a 100%)}

/* service cards */
.service-card{position:absolute;top:972px;width:448px;height:386px;background:var(--white)}
.service-card .photo{position:absolute;left:7px;top:0;width:435px;height:304px}
.service-card .label{position:absolute;left:27px;top:335px;font-family:var(--body);font-weight:500;font-size:22px;color:var(--black)}
.service-card .go{position:absolute;right:28px;top:333px}

/* counters */
.counter{position:absolute;top:1444px;width:212px;height:212px}
.counter .num{position:absolute;left:0;width:212px;top:60px;text-align:center;font-family:var(--head);font-weight:700;font-size:54px;color:var(--white);line-height:56px}
.counter .cap{position:absolute;left:20px;width:172px;top:124px;text-align:center;font-size:13px;line-height:20px;color:var(--white)}

/* reviews */
.review{position:absolute;top:1968px;width:292px;height:262px;border-radius:90px;background:var(--white);box-shadow:0 14px 40px rgba(0,0,0,.09)}
.review .mark{position:absolute;left:0;width:100%;top:34px;display:flex;justify-content:center}
.review p{position:absolute;left:36px;right:36px;top:94px;text-align:center;font-style:italic;font-weight:300;font-size:12.5px;line-height:24px;color:#555}
.review .who{position:absolute;left:0;width:100%;top:200px;text-align:center;font-family:var(--body);font-weight:500;font-size:20px;color:var(--black)}

/* posts */
.post{position:absolute;top:2340px;width:296px;height:316px;background:var(--white)}
.post .photo{position:absolute;left:7px;top:0;width:282px;height:196px}
.post .go{position:absolute;right:20px;top:186px}
.post .date{position:absolute;left:18px;top:220px;font-size:11px;color:var(--orange);font-weight:300}
.post h3{position:absolute;left:18px;top:242px;font-family:var(--body);font-weight:500;font-size:14px;color:var(--black)}
.post p{position:absolute;left:18px;right:30px;top:270px;font-size:10.5px;line-height:15px;color:var(--grey);font-weight:300}

/* newsletter */
.newsletter-title{position:absolute;left:143px;top:2752px;font-family:var(--head);font-weight:700;font-size:39px;color:var(--white)}
.email-field{position:absolute;left:143px;top:2860px;font-size:12px;color:var(--white)}
.email-line{position:absolute;left:143px;top:2904px;width:593px;height:1px;background:#555}
.btn-sub{left:610px;top:2845px;width:126px;height:42px;border-radius:21px;background:var(--orange);font-size:13px}

/* footer */
.social{position:absolute;top:3049px;width:46px;height:46px;border-radius:50%;background:var(--black)}
.contact-row{position:absolute;left:0;width:1200px;top:3132px;display:flex;justify-content:center;align-items:center;gap:16px;font-family:var(--head);font-weight:600;font-size:19px;color:var(--ink)}
.contact-row .item{display:flex;align-items:center;gap:10px}
.contact-row .sep{font-size:14px}
.footer-nav{position:absolute;left:0;width:1200px;top:3192px;text-align:center;font-family:var(--head);font-weight:700;font-size:24px;color:var(--black);word-spacing:4px}
.footer-nav span{margin:0 18px}
.copyright{position:absolute;left:0;width:1200px;top:3256px;text-align:center;font-size:13px;color:var(--grey);font-weight:300}
</style>
</head>
<body>

<header class="site-header">
  <div class="brand">GREY PRINT HOUSE</div>
  <nav class="main-nav">
    <a class="active" style="left:477px">HOME</a>
    <a style="left:550px">SERVICES</a>
    <a style="left:646px">CUSTOMER REVIEWS</a>
    <a style="left:808px">CONTACT</a>
  </nav>
  <svg class="header-phone" width="1200" height="70">
    <polygon points="885,0 1200,0 1200,70 922,70" fill="#131313"/>
    <path d="M942 26c2 0 3 3 4 5 0 1-1 2-2 3 1 3 3 5 6 6 1-1 2-2 3-2 2 1 5 2 5 4l-1 3c-9 1-18-8-17-17z" fill="#ec6a0e"/>
  </svg>
  <div class="header-phone-text">712.406.381</div>
</header>

<section class="hero" role="img" aria-label="Black and white photo of hands sorting printed proofs on a desk">
  <h1 class="hero-title">GREY PRINT HOUSE</h1>
  <div class="hero-sub">Printing &amp; graphic agency</div>
  <div class="btn btn-quote">REQUEST QUOTE
    <svg width="20" height="20" viewBox="0 0 20 20"><circle cx="10" cy="10" r="10" fill="#fff"/><path d="M8 5.5l5 4.5-5 4.5" stroke="#ec6a0e" stroke-width="2.6" fill="none"/></svg>
  </div>
  <div class="btn btn-more">LEARN MORE
    <svg width="20" height="20" viewBox="0 0 20 20"><circle cx="10" cy="10" r="10" fill="#fff"/><path d="M8 5.5l5 4.5-5 4.5" stroke="#131313" stroke-width="2.6" fill="none"/></svg>
  </div>
  <svg class="slide-arrow" style="left:70px" viewBox="0 0 52 52"><path d="M29 19l-7 7 7 7" stroke="#fff" stroke-width="2.5" fill="none"/></svg>
  <svg class="slide-arrow" style="left:1076px" viewBox="0 0 52 52"><path d="M23 19l7 7-7 7" stroke="#fff" stroke-width="2.5" fill="none"/></svg>
</section>

<h2 class="section-title" style="top:718px">WELCOME TO GREY PRINT HOUSE</h2>
<p class="welcome-text">Lorem ipsum dolor sit amet, consectetur adipiscing elit, sed do eiusmod tempor incididunt ut labore et dolore magna aliqua. Quis ipsum suspendisse ultrices gravida. Risus commodo viverra maecenas accumsan lacus vel facilisis. Lorem ipsum dolor sit ametconsectetur adipiscing elit, sed do eiusmod tempor incididunt ut labore et dolore magna aliqua ipsum suspendisse ultrices gravidaisus commodo viverra maecenas accumsan lacus vel facilisis.</p>

<div class="dark-band" style="top:1191px;height:551px" role="img" aria-label="Dark background with abstract black triangle shapes"></div>

<article class="service-card" style="left:143px">
  <div class="photo" role="img" aria-label="Black and white photo of a man checking print proofs at a desk" style="background:linear-gradient(135deg,#cfcfcf,#6d6d6d 60%,#3a3a3a)"></div>
  <div class="label">Printing</div>
  <svg class="go" width="36" height="36" viewBox="0 0 36 36"><circle cx="18" cy="18" r="18" fill="#131313"/><circle cx="18" cy="18" r="9" fill="#fff"/><path d="M16 13.5l4.5 4.5-4.5 4.5" stroke="#131313" stroke-width="2.4" fill="none"/></svg>
</article>
<article class="service-card" style="left:608px">
  <div class="photo" role="img" aria-label="Black and white photo of hands holding a design card in front of a monitor" style="background:linear-gradient(135deg,#3a3a3a,#8a8a8a 50%,#d0d0d0)"></div>
  <div class="label">Design</div>
  <svg class="go" width="36" height="36" viewBox="0 0 36 36"><circle cx="18" cy="18" r="18" fill="#131313"/><circle cx="18" cy="18" r="9" fill="#fff"/><path d="M16 13.5l4.5 4.5-4.5 4.5" stroke="#131313" stroke-width="2.4" fill="none"/></svg>
</article>

<div class="counter" style="left:143px">
  <svg width="212" height="212" viewBox="0 0 212 212"><circle cx="106" cy="106" r="101" fill="none" stroke="#fff" stroke-width="4"/><circle cx="106" cy="106" r="101" fill="none" stroke="#ec6a0e" stroke-width="4" stroke-dasharray="159 700" transform="rotate(-90 106 106) scale(1 -1) translate(0 -212)"/></svg>
  <div class="num">45</div><div class="cap">Years experience</div>
</div>
<div class="counter" style="left:376px">
  <svg width="212" height="212" viewBox="0 0 212 212"><circle cx="106" cy="106" r="101" fill="none" stroke="#fff" stroke-width="4"/><circle cx="106" cy="106" r="101" fill="none" stroke="#ec6a0e" stroke-width="4" stroke-dasharray="106 700" transform="rotate(-90 106 106) scale(1 -1) translate(0 -212)"/></svg>
  <div class="num">650</div><div class="cap">Colleagues</div>
</div>
<div class="counter" style="left:610px">
  <svg width="212" height="212" viewBox="0 0 212 212"><circle cx="106" cy="106" r="101" fill="none" stroke="#fff" stroke-width="4"/><circle cx="106" cy="106" r="101" fill="none" stroke="#ec6a0e" stroke-width="4" stroke-dasharray="210 700" transform="rotate(-90 106 106) scale(1 -1) translate(0 -212)"/></svg>
  <div class="num">500</div><div class="cap">already served customers</div>
</div>
<div class="counter" style="left:843px">
  <svg width="212" height="212" viewBox="0 0 212 212"><circle cx="106" cy="106" r="101" fill="none" stroke="#fff" stroke-width="4"/><circle cx="106" cy="106" r="101" fill="none" stroke="#ec6a0e" stroke-width="4" stroke-dasharray="63 700" transform="rotate(-90 106 106) scale(1 -1) translate(0 -212)"/></svg>
  <div class="num">300</div><div class="cap">already printed<br>paper sheets</div>
</div>

<h2 class="section-title" style="top:1838px">YOU DON'T HAVE TO TAKE OUR WORD FOR IT</h2>

<div class="review" style="left:145px">
  <div class="mark"><svg width="44" height="28" viewBox="0 0 44 28"><polygon points="8,0 20,0 12,28 0,28" fill="#ec6a0e"/><polygon points="30,0 42,0 34,28 22,28" fill="#ec6a0e"/></svg></div>
  <p>Grey Print House has been taking care of all our printing &amp; design work for some time now. You can go here for both small or larger quantities.</p>
  <div class="who">- Mira D</div>
</div>
<div class="review" style="left:455px">
  <div class="mark"><svg width="44" height="28" viewBox="0 0 44 28"><polygon points="8,0 20,0 12,28 0,28" fill="#ec6a0e"/><polygon points="30,0 42,0 34,28 22,28" fill="#ec6a0e"/></svg></div>
  <p>There is nothing you cannot print here! And that at the best prices. No comparison is necessary here.</p>
  <div class="who">- Joris T</div>
</div>
<div class="review" style="left:763px">
  <div class="mark"><svg width="44" height="28" viewBox="0 0 44 28"><polygon points="8,0 20,0 12,28 0,28" fill="#ec6a0e"/><polygon points="30,0 42,0 34,28 22,28" fill="#ec6a0e"/></svg></div>
  <p>We have all our printing &amp; design work done here. Fast and efficient service at an affordable price.</p>
  <div class="who">- Elke M</div>
</div>

<div class="dark-band" style="top:2473px;height:523px" role="img" aria-label="Dark background with abstract black triangle shapes"></div>

<article class="post" style="left:143px">
  <div class="photo" role="img" aria-label="Photo of a large format printer producing a print" style="background:linear-gradient(160deg,#bdbdbd,#5a5a5a 55%,#222)"></div>
  <svg class="go" width="20" height="20" viewBox="0 0 20 20"><circle cx="10" cy="10" r="10" fill="#131313"/><circle cx="10" cy="10" r="5" fill="#fff"/><path d="M9 7.5l2.5 2.5-2.5 2.5" stroke="#131313" stroke-width="1.6" fill="none"/></svg>
  <div class="date">Jan 29,2021</div>
  <h3>Lorem ipsum dolor sitetur adipiscing</h3>
  <p>Lorem ipsum dolor sit amet, consectetur adipiscing elit, sed do eiusmod tempor</p>
</article>
<article class="post" style="left:452px">
  <div class="photo" role="img" aria-label="Top view photo of a designer's wooden desk with computer and colour swatches" style="background:linear-gradient(160deg,#8a5a3a,#5e3b24 60%,#3b2516)"></div>
  <svg class="go" width="20" height="20" viewBox="0 0 20 20"><circle cx="10" cy="10" r="10" fill="#131313"/><circle cx="10" cy="10" r="5" fill="#fff"/><path d="M9 7.5l2.5 2.5-2.5 2.5" stroke="#131313" stroke-width="1.6" fill="none"/></svg>
  <div class="date">Jan 29,2021</div>
  <h3>Lorem ipsum dolor sitetur adipiscing</h3>
  <p>Lorem ipsum dolor sit amet, consectetur adipiscing elit, sed do eiusmod tempor</p>
</article>
<article class="post" style="left:761px">
  <div class="photo" role="img" aria-label="Black and white photo of hands holding a branding card in front of a monitor" style="background:linear-gradient(135deg,#3a3a3a,#8a8a8a 50%,#d4d4d4)"></div>
  <svg class="go" width="20" height="20" viewBox="0 0 20 20"><circle cx="10" cy="10" r="10" fill="#131313"/><circle cx="10" cy="10" r="5" fill="#fff"/><path d="M9 7.5l2.5 2.5-2.5 2.5" stroke="#131313" stroke-width="1.6" fill="none"/></svg>
  <div class="date">Jan 29,2021</div>
  <h3>Lorem ipsum dolor sitetur adipiscing</h3>
  <p>Lorem ipsum dolor sit amet, consectetur adipiscing elit, sed do eiusmod tempor</p>
</article>

<h2 class="newsletter-title">SUBSCRIBE TO OUR NEWSLETTER</h2>
<div class="email-field">Enter Email</div>
<div class="email-line"></div>
<div class="btn btn-sub">SUBSCRIBE
  <svg width="15" height="15" viewBox="0 0 20 20"><circle cx="10" cy="10" r="10" fill="#fff"/><path d="M8 5.5l5 4.5-5 4.5" stroke="#ec6a0e" stroke-width="2.6" fill="none"/></svg>
</div>

<footer>
  <div class="social" style="left:521px" aria-label="Social profile"></div>
  <div class="social" style="left:577px" aria-label="Social profile"></div>
  <div class="social" style="left:633px" aria-label="Social profile"></div>

  <div class="contact-row">
    <span class="item"><svg width="20" height="15" viewBox="0 0 20 15"><rect width="20" height="15" rx="2" fill="#ec6a0e"/><path d="M1 2l9 7 9-7" stroke="#fff" stroke-width="1.6" fill="none"/></svg>info@grijsdrukhuis.be</span>
    <span class="sep">|</span>
    <span class="item"><svg width="14" height="19" viewBox="0 0 14 19"><path d="M7 0a7 7 0 0 1 7 7c0 5-7 12-7 12S0 12 0 7a7 7 0 0 1 7-7z" fill="#ec6a0e"/><circle cx="7" cy="7" r="2.6" fill="#fff"/></svg>Lindelaan 42 - 3500 Hasselt - BE</span>
    <span class="sep">|</span>
    <span class="item"><svg width="17" height="17" viewBox="0 0 20 20"><path d="M2 1c2 0 4 4 4 6 0 1-1 2-2 3 2 3 4 5 7 6 1-1 2-2 3-2 2 0 6 2 6 4l-1 2C9 21-1 11 0 2z" fill="#ec6a0e"/></svg>712.406.381</span>
  </div>

  <nav class="footer-nav">HOME<span>/</span>SERVICES<span>/</span>CUSTOMER REVIEWS<span>/</span>CONTACT</nav>
  <div class="copyright">© 2021 by Grey Print House.All Rights Reserved &nbsp;|&nbsp; Privacy Policy &nbsp;| Terms and use</div>
</footer>

</body>
</html>
```